Restaurant, Nightclub

It's a Restaurant come nightclub. Our sign Tamsel is white letters with blue edging on a black back ground.

Industry/Entity Type

Restaurant

Contact Information for Business Card

Tamsel Stevenage Ltd
14 Larkfield Row
Stevenage Herts KX7 2PW

```html
<!DOCTYPE html>
<html lang="en">
<head>
<meta charset="utf-8">
<title>Tamsel Stevenage Ltd – Business Cards</title>
<link rel="stylesheet" href="https://fonts.googleapis.com/css2?family=Arimo:wght@400;700&display=swap">
<style>
  :root {
    --backdrop: #3a3a3a;
    --card-white: #ffffff;
    --night-black: #000000;
    --sky-blue: #2fb3e8;
    --logo-grey: #b5b8bb;
    --ink-light: #ffffff;
  }
  * { margin: 0; padding: 0; box-sizing: border-box; }
  html, body {
    width: 1200px;
    height: 750px;
    overflow: hidden;
    background: var(--backdrop);
    font-family: "Arimo", Arial, sans-serif;
  }
  .card {
    position: absolute;
    top: 218px;
    width: 494px;
    height: 282px;
    border-radius: 18px;
    overflow: hidden;
    background: var(--card-white);
  }
  .card--night { left: 90px; }
  .card--sky { left: 620px; }
  .card__wave {
    position: absolute;
    inset: 0;
    width: 100%;
    height: 100%;
  }
  .card__brand {
    position: absolute;
    left: 14px;
    top: 138px;
    width: 222px;
    text-align: center;
    font-weight: 700;
    font-size: 44px;
    letter-spacing: 1px;
    color: var(--logo-grey);
    line-height: 1;
  }
  .card__details {
    position: absolute;
    left: 296px;
    top: 106px;
    width: 176px;
    text-align: center;
    color: var(--ink-light);
  }
  .card__company {
    font-size: 15px;
    font-weight: 400;
    margin-bottom: 14px;
  }
  .card__address {
    font-size: 11px;
    line-height: 14px;
    font-style: normal;
  }
</style>
</head>
<body>

  <section class="card card--night">
    <svg class="card__wave" viewBox="0 0 494 282" aria-hidden="true">
      <path d="M204 0 C219 60 254 90 259 150 S269 240 269 282 L494 282 L494 0 Z" fill="var(--night-black)"/>
      <g fill="none" stroke="var(--sky-blue)" stroke-width="4">
        <path d="M208 -2 C223 60 258 90 263 150 S273 240 273 284"/>
        <path d="M215 -2 C230 60 265 90 270 150 S280 240 280 284"/>
        <path d="M222 -2 C237 60 272 90 277 150 S287 240 287 284"/>
        <path d="M229 -2 C244 60 279 90 284 150 S294 240 294 284"/>
      </g>
    </svg>
    <div class="card__brand">Tamsel</div>
    <div class="card__details">
      <h1 class="card__company">Tamsel Stevenage Ltd</h1>
      <address class="card__address">14 Larkfield Row<br>Stevenage Herts KX7 2PW</address>
    </div>
  </section>

  <section class="card card--sky">
    <svg class="card__wave" viewBox="0 0 494 282" aria-hidden="true">
      <path d="M204 0 C219 60 254 90 259 150 S269 240 269 282 L494 282 L494 0 Z" fill="var(--sky-blue)"/>
      <g fill="none" stroke="var(--night-black)" stroke-width="4">
        <path d="M208 -2 C223 60 258 90 263 150 S273 240 273 284"/>
        <path d="M215 -2 C230 60 265 90 270 150 S280 240 280 284"/>
        <path d="M222 -2 C237 60 272 90 277 150 S287 240 287 284"/>
        <path d="M229 -2 C244 60 279 90 284 150 S294 240 294 284"/>
      </g>
    </svg>
    <div class="card__brand">Tamsel</div>
    <div class="card__details">
      <h2 class="card__company">Tamsel Stevenage Ltd</h2>
      <address class="card__address">14 Larkfield Row<br>Stevenage Herts KX7 2PW</address>
    </div>
  </section>

</body>
</html>
```